Harbor Logistics Business card and letterhead
Professional business card
Professional
Calvin Marsh
Director of Operations
4538 E 61st Pl
Maple Grove, KS 66417-3814
cmarsh@harborlogisticsco.example
http://www.harborlogisticsco.example
Looking for something clean, professional, and simple. Fonts are optional, just flow with fonts in logo
On the back we would like the mission of "Improving people's lives" printed in some design. We would like the background to be a solid design from a logo color with white writing
This is our corporate logo

```html
<!DOCTYPE html>
<html lang="en">
<head>
<meta charset="utf-8">
<title>Harbor Logistics Stationery</title>
<link rel="stylesheet" href="https://fonts.googleapis.com/css2?family=Arimo:wght@400;700&display=swap">
<style>
  :root {
    --page: #ececec;
    --board: #ffffff;
    --board-line: #d6d6d6;
    --paper: #ffffff;
    --paper-edge: #dcdcdc;
    --band-light: #8fd1c8;
    --band-mid: #2f7fc4;
    --band-deep: #1b2f8c;
    --band-dark: #0b1238;
    --brand: #1a2f7c;
    --mark: #2f7fc4;
    --ink: #3a3a3a;
    --card-back: #0a1233;
    --glow: #3b76d6;
  }
  * { margin: 0; padding: 0; box-sizing: border-box; }
  html, body { width: 1200px; height: 741px; overflow: hidden; }
  body { background: var(--page); font-family: "Arimo", Arial, sans-serif; color: var(--ink); position: relative; }

  .board { position: absolute; left: 12px; top: 12px; width: 1176px; height: 717px; background: var(--board); border: 1px solid var(--board-line); }

  .sheet { position: absolute; background: var(--paper); border: 1px solid var(--paper-edge); box-shadow: 0 1px 3px rgba(0,0,0,.12); overflow: hidden; }

  .band { position: absolute; background: linear-gradient(90deg, var(--band-light) 0%, var(--band-mid) 30%, var(--band-deep) 65%, var(--band-dark) 100%); }

  .brand { position: absolute; display: flex; align-items: center; gap: 6px; }
  .brand-dot { border-radius: 50%; background: var(--mark); flex: none; }
  .brand-name { font-weight: 700; color: var(--brand); white-space: nowrap; }

  .small-text { position: absolute; font-size: 6px; line-height: 1.45; color: var(--ink); white-space: nowrap; }

  /* Envelope front */
  .envelope-front { left: 60px; top: 156px; width: 528px; height: 281px; }
  .envelope-front .band { left: 84px; top: 10px; right: 0; height: 30px; }
  .envelope-front .brand { left: 16px; top: 14px; }
  .envelope-front .brand-dot { width: 42px; height: 42px; }
  .envelope-front .brand-name { position: absolute; left: 0; top: 48px; font-size: 15px; }
  .envelope-front .small-text { left: 18px; top: 98px; }

  /* Envelope back */
  .envelope-back { left: 60px; top: 461px; width: 528px; height: 223px; }
  .envelope-back svg { position: absolute; inset: 0; }

  /* Letterhead */
  .letterhead { left: 631px; top: 91px; width: 324px; height: 593px; }
  .letterhead .band { left: 66px; top: 17px; right: 0; height: 24px; }
  .letterhead .brand-dot { position: absolute; left: 12px; top: 12px; width: 36px; height: 36px; border-radius: 50%; background: var(--mark); }
  .letterhead .brand-name { position: absolute; left: 12px; top: 53px; font-size: 12px; }
  .letterhead .small-text { left: 12px; top: 80px; font-size: 5px; }
  .letterhead .watermark { position: absolute; left: 190px; top: 420px; width: 120px; height: 120px; border-radius: 50%; background: #f1f2f3; }

  /* Business card front */
  .card-front { left: 960px; top: 197px; width: 156px; height: 115px; }
  .card-front .band { left: 24px; top: 12px; right: 0; height: 14px; }
  .card-front .brand-dot { position: absolute; left: 6px; top: 8px; width: 18px; height: 18px; border-radius: 50%; background: var(--mark); }
  .card-front .brand-name { position: absolute; left: 6px; top: 29px; font-size: 7px; }
  .card-front .small-text { left: 6px; top: 54px; font-size: 4.2px; }

  /* Business card back */
  .card-back { left: 960px; top: 329px; width: 156px; height: 115px; border-color: var(--card-back);
    background: radial-gradient(circle at 50% 40%, var(--glow) 0%, #1c3a8a 22%, var(--card-back) 55%); }
  .card-back .mission { position: absolute; left: 0; right: 0; top: 78px; text-align: center; font-size: 5px; color: #ffffff; letter-spacing: .2px; }
</style>
</head>
<body>
  <div class="board"></div>

  <section class="sheet envelope-front" aria-label="Envelope front">
    <div class="band"></div>
    <div class="brand"><span class="brand-dot"></span><span class="brand-name">Harbor Logistics</span></div>
    <p class="small-text">4538 E 61st Pl<br>Maple Grove, KS 66417-3814</p>
  </section>

  <section class="sheet envelope-back" aria-label="Envelope back">
    <svg width="528" height="223" viewBox="0 0 528 223">
      <polyline points="0,6 40,8 250,104 278,104 488,8 528,6" fill="none" stroke="#b9b9b9" stroke-width="1"/>
      <circle cx="264" cy="80" r="12" fill="var(--mark)"/>
    </svg>
  </section>

  <section class="sheet letterhead" aria-label="Letterhead">
    <div class="band"></div>
    <span class="brand-dot"></span>
    <span class="brand-name">Harbor Logistics</span>
    <p class="small-text">4538 E 61st Pl, Maple Grove, KS 66417-3814<br>Phone (913) 555-0148 | http://www.harborlogisticsco.example</p>
    <div class="watermark"></div>
  </section>

  <section class="sheet card-front" aria-label="Business card front">
    <div class="band"></div>
    <span class="brand-dot"></span>
    <span class="brand-name">Harbor Logistics</span>
    <p class="small-text">Calvin Marsh<br>Director of Operations<br>4538 E 61st Pl, Maple Grove, KS 66417-3814<br>Phone (913) 555-0148 | cmarsh@harborlogisticsco.example</p>
  </section>

  <section class="sheet card-back" aria-label="Business card back">
    <p class="mission">Improving people's lives</p>
  </section>
</body>
</html>
```